OKRUVI card Technical Architecture

Hello everyone OKRUVI: It is a consulting firm in Architecture and Construction. I require a card duplexing, sober, elegant, classic but not boring. Update 1: Use the following data for the card. Name: Rodrigo Salcedo Mauricio Quintana Position: COO Twitter: @okruviTB Homepage: okruvi.net home address not include the participation of all thank you.

Target Market(s)

Construction companies, Architects and Consulting Engineers

Industry/Entity Type

Consulting

Contact Information for Business Card

Los campos que debe tener:
Nombre, Cargo, email, homepage y twitter

Font styles to use
Serif
Sans Serif
Other font styles liked:
• Me gustan playfair display, open sans y roboto, pero estoy sujeto a sus propuestas

Requirements
Must have
• Colors: Present combined proposals in white, red, gray and black Update 1: The two names must be clearly differentiated from the two surnames
Nice to have
• They are free to present their best proposals. I will bring them immediate feedback to the extent you can go see their designs. Complete data for card and logo files will give the winner the

```html
<!DOCTYPE html>
<html lang="es">
<head>
<meta charset="utf-8">
<title>OKRUVI – Tarjeta de presentación</title>
<link href="https://fonts.googleapis.com/css2?family=Open+Sans:wght@300;400;600;700&display=swap" rel="stylesheet">
<style>
  :root{
    --bg:#e9e7e4;
    --white:#ffffff;
    --paper:#f4f4f4;
    --red:#d3262b;
    --red-dark:#a8181d;
    --ink:#1c1c1c;
    --graphite:#262b30;
    --black:#111111;
    --muted:#555;
  }
  *{box-sizing:border-box;margin:0;padding:0}
  html,body{width:1200px;height:1023px;overflow:hidden;background:var(--bg);font-family:"Open Sans",Arial,sans-serif}
  .canvas{position:relative;width:1200px;height:1023px}
  .card{position:absolute;left:250px;width:700px;height:400px;border-radius:14px;overflow:hidden;box-shadow:0 10px 30px rgba(0,0,0,.18)}
  .card--front{top:70px;background:linear-gradient(180deg,var(--white),var(--paper))}
  .card--back{top:543px;background:radial-gradient(ellipse at 50% 45%,#3a3a3a 0%,#1a1a1a 55%,var(--black) 100%)}

  /* front */
  .edge-band{position:absolute;right:0;top:0;width:26px;height:100%}
  .edge-band__red{height:44%;background:var(--red)}
  .edge-band__dark{height:56%;background:var(--graphite)}
  .brand{position:absolute;display:flex;flex-direction:column;align-items:flex-start}
  .brand__row{display:flex;align-items:center;gap:16px}
  .brand__dot{width:30px;height:30px;border-radius:50%;background:var(--red)}
  .brand__name{font-weight:300;letter-spacing:.34em;line-height:1}
  .brand__rule{height:1px;background:var(--red)}
  .brand__tag{font-weight:400;letter-spacing:.38em;color:var(--red);text-transform:uppercase}
  .card--front .brand{left:60px;top:148px}
  .card--front .brand__name{font-size:52px;color:var(--ink)}
  .card--front .brand__rule{width:290px;margin:12px 0 7px 46px}
  .card--front .brand__tag{font-size:11px;margin-left:46px;color:var(--ink)}
  .divider{position:absolute;left:395px;top:95px;width:1px;height:210px;background:var(--red)}
  .contact{position:absolute;left:425px;top:86px;width:240px}
  .contact__given{font-size:19px;font-weight:700;color:var(--red);line-height:1.2}
  .contact__family{font-size:18px;font-weight:400;color:var(--ink);line-height:1.2}
  .contact__role{font-size:10.5px;color:var(--red);margin-top:3px}
  .contact__list{list-style:none;margin-top:26px}
  .contact__item{display:flex;align-items:center;gap:12px;font-size:13px;color:var(--ink);height:27px}
  .contact__icon{width:15px;height:15px;flex:none}

  /* back */
  .card--back .brand{left:190px;top:130px}
  .card--back .brand__name{font-size:60px;color:var(--white)}
  .card--back .brand__dot{width:34px;height:34px}
  .card--back .brand__rule{width:320px;margin:14px 0 8px 50px}
  .card--back .brand__tag{font-size:12px;margin-left:50px}
</style>
</head>
<body>
<main class="canvas">

  <section class="card card--front" aria-label="Anverso de la tarjeta">
    <div class="brand">
      <div class="brand__row">
        <span class="brand__dot"></span>
        <span class="brand__name">OKRUVI</span>
      </div>
      <div class="brand__rule"></div>
      <span class="brand__tag">Arquitectura técnica</span>
    </div>

    <div class="divider"></div>

    <div class="contact">
      <p class="contact__given">Rodrigo Salcedo</p>
      <p class="contact__family">Mauricio Quintana</p>
      <p class="contact__role">Director de Operaciones</p>
      <ul class="contact__list">
        <li class="contact__item">
          <svg class="contact__icon" viewBox="0 0 16 16"><circle cx="8" cy="8" r="7" fill="none" stroke="#d3262b" stroke-width="1.4"/><path d="M5.5 4.5l1.5 1.8-.8 1c.6 1.2 1.4 2 2.5 2.5l1-.8 1.8 1.5-.8 1c-3 0-6.2-3.2-6.2-6.2z" fill="#d3262b"/></svg>
          (+571) 555 010 2020
        </li>
        <li class="contact__item">
          <svg class="contact__icon" viewBox="0 0 16 16"><rect x="1" y="3" width="14" height="10" rx="1" fill="#d3262b"/><path d="M1.5 3.5L8 9l6.5-5.5" fill="none" stroke="#fff" stroke-width="1.2"/></svg>
          info@okruvi.net
        </li>
        <li class="contact__item">
          <svg class="contact__icon" viewBox="0 0 16 16" fill="none" stroke="#d3262b" stroke-width="1.2"><circle cx="8" cy="8" r="6.5"/><ellipse cx="8" cy="8" rx="3" ry="6.5"/><path d="M1.5 8h13M2.5 4.8h11M2.5 11.2h11"/></svg>
          www.okruvi.net
        </li>
        <li class="contact__item">
          <svg class="contact__icon" viewBox="0 0 16 16"><circle cx="8" cy="8" r="6.5" fill="#d3262b"/></svg>
          @okruviTB
        </li>
      </ul>
    </div>

    <div class="edge-band">
      <div class="edge-band__red"></div>
      <div class="edge-band__dark"></div>
    </div>
  </section>

  <section class="card card--back" aria-label="Reverso de la tarjeta">
    <div class="brand">
      <div class="brand__row">
        <span class="brand__dot"></span>
        <span class="brand__name">OKRUVI</span>
      </div>
      <div class="brand__rule"></div>
      <span class="brand__tag">Arquitectura técnica</span>
    </div>
  </section>

</main>
</body>
</html>
```